Catchy Cards for Hospital

I run a rural hospital in Texas called Pellor Valley Hospital and am in need of contemporary business cards for all of my Department Heads. While our logo is somewhat simplistic, I don't have the option of changing it at this time, so anything to make the rest of the card present the appearance of a modern, professional healthcare facility would be great. Although the attached files are in black, our hospital colors are in a copper brown and black. I need to be able to change the name and title on the card so I can get cards printed for various department heads.

Target Market(s)

Referring physicians, large hospital systems, national organizations, state and federal government

Industry/Entity Type

Hospital

Contact Information for Business Card

Name Dale Hoskin
Title CEO

Phone: Main 325-555-0147 & Direct xxxxxx
Fax xxxxx
dale.hoskin@pellorvh.example
382 Wimble Street Box 415
Dunmere, Calvera 76902

Font styles to use
Serif

Colors
f48340

Requirements
Must have
• Clean crisp lines and ability to modify names, titles and emails
• On the back "PellorValleyHospital.Example
Nice to have
• Needs to be in line with logo, which is a bit dated and not too appealing, but I'm hoping that the rest of the card can make up for that fact just a little bit.
• Hospital's colors are a copper brown, black and white
Should not have
• Shapes or anything distracting

```html
<!DOCTYPE html>
<html lang="en">
<head>
<meta charset="utf-8">
<title>Pellor Valley Hospital – Business Card</title>
<link href="https://fonts.googleapis.com/css2?family=Open+Sans:wght@400;600&display=swap" rel="stylesheet">
<style>
  :root {
    --copper: #f48340;
    --ink: #000000;
    --paper: #ffffff;
    --backdrop: #2e2e2e;
  }
  * { margin: 0; padding: 0; box-sizing: border-box; }
  html, body { width: 1200px; height: 900px; overflow: hidden; }
  body {
    background: var(--backdrop);
    font-family: "Open Sans", Arial, sans-serif;
    position: relative;
  }
  .card {
    position: absolute;
    left: 320px;
    width: 560px;
    height: 320px;
    overflow: hidden;
  }
  .card-back {
    top: 100px;
    background: var(--copper);
    color: var(--paper);
  }
  .brand-name {
    position: absolute;
    left: 0; right: 0;
    top: 96px;
    text-align: center;
    font-size: 40px;
    font-weight: 600;
    line-height: 1.1;
  }
  .back-url {
    position: absolute;
    left: 0; right: 0;
    top: 236px;
    text-align: center;
    font-size: 15px;
    letter-spacing: 1px;
  }
  .card-front {
    top: 470px;
    background: var(--paper);
  }
  .name-block {
    position: absolute;
    left: 0; top: 64px;
    width: 226px; height: 122px;
    background: var(--ink);
    padding: 30px 0 0 28px;
  }
  .person-name {
    color: var(--copper);
    font-size: 22px;
    font-weight: 600;
    line-height: 1.1;
  }
  .person-title {
    color: var(--paper);
    font-size: 13px;
    margin-top: 4px;
  }
  .contact-panel {
    position: absolute;
    left: 232px; top: 74px;
    right: 0; height: 206px;
    background: var(--copper);
    color: var(--paper);
  }
  .divider {
    position: absolute;
    left: 26px; top: 16px;
    width: 2px; height: 104px;
    background: var(--paper);
  }
  .address {
    position: absolute;
    left: 58px; top: 14px;
    font-size: 14px;
    line-height: 1.3;
  }
  .contact-list {
    position: absolute;
    left: 44px; top: 66px;
    list-style: none;
    font-size: 14px;
    line-height: 1.45;
  }
  .contact-list li { display: flex; align-items: center; gap: 10px; }
  .contact-list svg { width: 14px; height: 14px; flex: none; fill: var(--paper); }
</style>
</head>
<body>

<section class="card card-back">
  <div class="brand-name">Pellor Valley<br>Hospital</div>
  <div class="back-url">www.PellorValleyHospital.Example</div>
</section>

<section class="card card-front">
  <div class="name-block">
    <div class="person-name">Marisol Avena</div>
    <div class="person-title">Doctor</div>
  </div>
  <div class="contact-panel">
    <div class="divider"></div>
    <div class="address">382 Wimble St.<br>Dunmere, Calvera 76902</div>
    <ul class="contact-list">
      <li>
        <svg viewBox="0 0 16 16" aria-hidden="true"><path d="M4 1l3 3-2 2c1 2 3 4 5 5l2-2 3 3-2 3C7 15 1 9 1 3z"/></svg>
        (555) 555-0147
      </li>
      <li>
        <svg viewBox="0 0 16 16" aria-hidden="true"><rect x="4" y="1" width="8" height="4"/><rect x="1" y="6" width="14" height="6" rx="1"/><rect x="4" y="10" width="8" height="5"/></svg>
        (555) 555-0198
      </li>
      <li>
        <svg viewBox="0 0 16 16" aria-hidden="true"><path d="M1 3h14v10H1z M1 3l7 6 7-6" fill="none" stroke="#fff" stroke-width="1.5"/></svg>
        info@PellorValleyHospital.Example
      </li>
      <li>
        <svg viewBox="0 0 16 16" aria-hidden="true"><circle cx="8" cy="8" r="6.5" fill="none" stroke="#fff" stroke-width="1.5"/><path d="M1.5 8h13M8 1.5c-3 3-3 10 0 13M8 1.5c3 3 3 10 0 13" fill="none" stroke="#fff" stroke-width="1.2"/></svg>
        www.PellorValleyHospital.Example
      </li>
    </ul>
  </div>
</section>

</body>
</html>
```